High Quality Flyer Design For Real Estate Website

I require a double sided flyer for the website hellohomekeys.net.

The flyer size should be A5.

The flyer must be fresh and up to date and go with the theme of the website.
Updates

Old flyer attachment was missing, but is now attached.

Target Market(s)

Landlords and people looking to buy or sell their house of all age groups

Industry/Entity Type

Real Estate

Font styles to use
Sans Serif

Requirements
Must have
• The main colour of the flyer should be the yellow used on the website.

The logo from the website should also be used (attached)

The text included on the old flyer must be on the new flyer (see attachment)

The flyer should take the reader through a process (see old attached flyer) and make them feel that using the website is very simple.

Nice to have

```html
<!DOCTYPE html>
<html lang="en">
<head>
<meta charset="utf-8">
<title>hellohomekeys.net – A5 Flyer</title>
<link href="https://fonts.googleapis.com/css2?family=PT+Sans:wght@400;700&display=swap" rel="stylesheet">
<style>
  :root{
    --yellow:#fdc70c;
    --yellow-light:#ffe44d;
    --yellow-deep:#f0a800;
    --black:#0d0d0d;
    --ink:#111111;
    --white:#ffffff;
    --steel:#5d646b;
    --steel-dark:#2a2e33;
  }
  *{margin:0;padding:0;box-sizing:border-box}
  html,body{width:867px;height:1200px;overflow:hidden;background:var(--white)}
  body{position:relative;font-family:"PT Sans",Arial,sans-serif}

  .flyer{position:absolute;left:70px;width:722px;overflow:hidden}
  .flyer--front{top:70px;height:512px;background:var(--black)}
  .flyer--back{top:592px;height:543px;background:linear-gradient(#1a1a1a,#050505)}

  /* front */
  .hero-photo{position:absolute;left:0;top:0;width:722px;height:372px;
    background:radial-gradient(ellipse at 62% 62%,#fff6b0 0%,#e6d23a 14%,#7e9a22 38%,#2f4a1c 62%,#141c14 100%)}
  .tab{position:absolute;left:0;background:var(--yellow);color:var(--ink);font-weight:700;
    text-transform:uppercase;font-size:27px;line-height:29px;padding-left:38px;display:flex;align-items:center;
    border-radius:0 46px 0 0;box-shadow:0 3px 6px rgba(0,0,0,.35)}
  .tab--sell{top:128px;height:72px;width:327px}
  .tab--free{top:218px;height:42px;width:302px}
  .tab--bye{top:278px;height:77px;width:290px}

  .contact-bar{position:absolute;top:372px;left:0;width:722px;height:31px;display:flex;gap:6px;background:var(--black)}
  .contact-bar span{background:var(--yellow);color:var(--ink);font-weight:700;font-size:15px;display:flex;align-items:center}
  .contact-email{width:305px;padding-left:38px;border-radius:0 0 22px 0}
  .contact-phones{flex:1;padding-left:18px;border-radius:22px 0 0 0}

  .brand-bar{position:absolute;top:403px;left:0;width:722px;height:109px;background:linear-gradient(#1b1b1b,#000)}
  .brand-name{position:absolute;left:36px;top:38px;display:flex;align-items:center;gap:10px;
    color:var(--yellow);font-weight:700;font-size:28px}
  .brand-name i{display:block;width:22px;height:22px;background:var(--yellow)}
  .brand-url{position:absolute;right:30px;top:48px;color:var(--yellow);font-weight:700;font-size:24px}

  /* back */
  .offer-panel{position:absolute;left:0;top:0;width:722px;height:240px;background:linear-gradient(var(--yellow-light),var(--yellow))}
  .offer-text{position:absolute;left:32px;top:50px;width:350px;color:var(--ink);font-weight:700;font-size:22.5px;line-height:30px}
  .offer-text strong{font-size:26px}
  .site-preview{position:absolute;left:362px;top:12px;width:360px;height:225px;border-radius:8px 8px 2px 2px;
    background:linear-gradient(#3a3d41 0 6px,#e8e9ea 6px 88%,#b5b8bb 88% 92%,#d9dbdd 92%)}
  .back-url{position:absolute;top:250px;left:0;width:722px;text-align:center;color:var(--yellow);font-weight:700;font-size:24px;letter-spacing:1px}
  .steps-panel{position:absolute;left:30px;top:292px;width:662px;height:228px;
    background:radial-gradient(ellipse at 50% 20%,#7a8289,var(--steel) 45%,var(--steel-dark));border:1px solid #888}
  .step{position:absolute;top:56px;width:204px;height:92px;border-radius:10px;
    background:linear-gradient(var(--yellow-light),var(--yellow-deep));color:var(--ink);font-weight:700;font-size:14px;
    line-height:17px;text-align:center;padding:16px 12px 0;box-shadow:0 2px 5px rgba(0,0,0,.45)}
  .step:nth-of-type(1){left:7px}
  .step:nth-of-type(2){left:225px}
  .step:nth-of-type(3){left:442px}
  .step-label{position:absolute;top:-24px;left:34px;width:136px;height:30px;background:var(--black);color:var(--yellow);
    font-size:17px;font-weight:400;display:flex;align-items:center;justify-content:center;gap:8px;border-radius:14px 3px 14px 3px}
  .step-label b{display:inline-flex;width:22px;height:22px;border-radius:50%;background:var(--white);color:var(--ink);
    align-items:center;justify-content:center;font-size:15px}
  .steps-note{position:absolute;left:10px;right:10px;top:168px;text-align:center;color:var(--white);font-weight:700;font-size:15.5px;line-height:21px}
</style>
</head>
<body>

<section class="flyer flyer--front">
  <div class="hero-photo" role="img" aria-label="Photo of a hand lowering a small model house into an open palm against a glowing green and yellow sky"></div>
  <div class="tab tab--sell">Sell or rent your<br>property</div>
  <div class="tab tab--free">Commision free</div>
  <div class="tab tab--bye">&amp; Say bye bye to<br>estate agents</div>
  <div class="contact-bar">
    <span class="contact-email">info@hellohomekeys.net</span>
    <span class="contact-phones">Tel # 01632 960418 (mon-fri 9-5)&nbsp; Mob # 07700 900263</span>
  </div>
  <div class="brand-bar">
    <div class="brand-name"><i></i>hellohomekeys.net</div>
    <div class="brand-url">www.hellohomekeys.net</div>
  </div>
</section>

<section class="flyer flyer--back">
  <div class="offer-panel">
    <p class="offer-text">For a limited time only, we are offering you the oppotunity to use our <strong>NEW WEBSITE</strong> for <strong>FREE</strong> to Buy, sell or Let your next property.</p>
  </div>
  <div class="site-preview" role="img" aria-label="Laptop displaying the hellohomekeys.net website home page"></div>
  <div class="back-url">www.hellohomekeys.net</div>
  <div class="steps-panel">
    <div class="step"><span class="step-label">Step <b>1</b></span>Go to<br>hellohomekeys.net</div>
    <div class="step"><span class="step-label">Step <b>1</b></span>Create an account</div>
    <div class="step"><span class="step-label">Step <b>1</b></span>Upload your property using the simple step by step process</div>
    <p class="steps-note">Once your property is uploaded, any interested Buyers and Tenants can contact you directly, to negotiate a price SAVING You £1000's in Estate Agent Fees.</p>
  </div>
</section>

</body>
</html>
```